Packaging for a gift bag make your own dog biscuits.

I am looking for someone who can design me a card design that can be attached to a gift bag containing all the ingredients someone would need in order to make their own dog biscuits. The dog buscuits will be chocolate bone shaped biscuits. My company name is Fennel Pup Pantry and i have attached a copy of the company logo to this description. I would like something classy and artisan but not too child like. The design i am looking for is purely the design that will capture the customer all the leagl informastion will be at the back to there is no need to worry about any of this at this stage. The design would need to fit a rectangular or similar shaped piece of card no bigger than 9cm - 14cm I have also attached some pictures of a similar product to give you an idea. The gift bags they will be attached to will be 11cm x 16cm.
The gift bags will be red so it would be nice for the design to compliment this. Ok so just to add a slight complication I am now considering a tent carton as an alternative. I have a picture to a similar type product below. The box I have here is 19cm high (11cm been the square before the tent) 9.5cm width and 7cm girth.

Target Market(s)

Dog lovers, people who visit artisan markets and like to spend time with their much loved fur family.

Font styles to use
Decorative

Colors

Designer to choose colors to be used in the design.

Requirements
Must have
• A classy but artisan design that will attract both adults and kids and may also be something that could be purchased as a gift.
Nice to have
• Something to compliment the red gift bag. The logo visible somewhere on the design and the design in keeping with the company logo.
Should not have
• Any familiar cartoon characters, or a child like feel

```html
<!DOCTYPE html>
<html lang="en">
<head>
<meta charset="utf-8">
<title>Fennel Pup Pantry – Make Your Own Dog Biscuits Baking Kit</title>
<link href="https://fonts.googleapis.com/css2?family=Baumans&family=Gochi+Hand&display=swap" rel="stylesheet">
<style>
  :root {
    --page: #ffffff;
    --mint: #cbe9d9;
    --mint-text: #d4f0de;
    --carton-edge: #6b4330;
    --cap: #4a2a1a;
    --wood: #573727;
    --wood-dark: #43291c;
    --bone: #ecdcc3;
    --ink-brown: #5b3a26;
    --screw: #a9b8c8;
    --badge: #d9b98f;
  }
  * { margin: 0; padding: 0; box-sizing: border-box; }
  html, body { width: 899px; height: 1200px; overflow: hidden; background: var(--page); }
  .canvas { position: relative; width: 899px; height: 1200px; }
  .carton-shapes { position: absolute; inset: 0; }
  .label {
    position: absolute; left: 0; width: 899px; text-align: center;
    font-family: "Baumans", sans-serif; line-height: 1;
  }
  .headline { color: var(--mint-text); font-size: 38px; letter-spacing: 5px; }
  .headline--top { top: 552px; }
  .headline--dog { top: 792px; font-size: 42px; }
  .headline--biscuits { top: 842px; font-size: 42px; }
  .bone-text {
    position: absolute; left: 262px; width: 380px; text-align: center;
    font-family: "Gochi Hand", cursive; color: var(--ink-brown);
    font-size: 34px; line-height: 40px;
    top: 658px;
  }
  .brand-name {
    position: absolute; left: 333px; top: 155px; width: 264px; height: 264px;
    display: flex; align-items: center; justify-content: center; text-align: center;
    font-family: "Baumans", sans-serif; font-size: 40px; line-height: 1.1;
    color: var(--ink-brown); padding: 0 30px;
  }
  .kit-title { top: 1044px; color: var(--ink-brown); font-size: 44px; letter-spacing: 5px; }
  .kit-note { top: 1098px; color: var(--ink-brown); font-size: 20px; letter-spacing: 1px; font-family: "Baumans", sans-serif; }
</style>
</head>
<body>
<main class="canvas">
  <svg class="carton-shapes" width="899" height="1200" viewBox="0 0 899 1200" aria-hidden="false">
    <!-- carton body -->
    <polygon class="carton-outline" points="176,0 714,0 714,508 740,526 740,1182 166,1182 166,520 176,512" fill="var(--carton-edge)"/>
    <rect class="top-panel" x="188" y="56" width="516" height="464" fill="var(--mint)"/>
    <polygon class="top-cap" points="176,0 714,0 714,58 176,58" fill="var(--cap)"/>
    <rect class="bottom-panel" x="178" y="890" width="550" height="280" fill="var(--mint)"/>
    <rect class="wood-band" x="166" y="520" width="574" height="370" fill="var(--wood)" role="img" aria-label="Dark wood plank texture"/>
    <line class="plank-seam" x1="166" y1="706" x2="740" y2="706" stroke="var(--wood-dark)" stroke-width="4"/>
    <!-- screws -->
    <circle class="screw" cx="206" cy="608" r="9" fill="var(--screw)"/>
    <circle class="screw" cx="695" cy="608" r="9" fill="var(--screw)"/>
    <circle class="screw" cx="206" cy="792" r="9" fill="var(--screw)"/>
    <circle class="screw" cx="695" cy="792" r="9" fill="var(--screw)"/>
    <!-- bone label -->
    <path class="bone" fill="var(--bone)"
      d="M318,660 C290,620 250,640 258,672 C230,684 236,728 266,732 C256,770 300,786 320,752
         L584,752 C604,786 648,770 638,732 C668,728 674,684 646,672 C654,640 614,620 586,660 Z"/>
    <!-- brand badge -->
    <circle class="brand-badge" cx="465" cy="287" r="132" fill="var(--badge)"/>
  </svg>

  <div class="brand-name">Fennel Pup Pantry</div>

  <div class="label headline headline--top">MAKE YOUR OWN</div>
  <div class="bone-text">chocolate<br>bone shaped</div>
  <div class="label headline headline--dog">DOG</div>
  <div class="label headline headline--biscuits">BISCUITS</div>

  <div class="label kit-title">BAKING KIT</div>
  <div class="label kit-note">contains all needed ingredients</div>
</main>
</body>
</html>
```